Business Card Design Project

We are an agricultural business based in Brisbane.
We design, manage and operate regional saleyards. Our logo is green/silver in colour and details of our business can be found on our website www.tovrak.com.au

Just wanting a corporate design for some business cards and include name, position, contact details.

Thanks

```html
<!DOCTYPE html>
<html lang="en">
<head>
<meta charset="utf-8">
<title>Tovrak Regional – Business Card</title>
<link rel="stylesheet" href="https://fonts.googleapis.com/css2?family=Oswald:wght@300;400;500;600&display=swap">
<style>
  :root {
    --page: #ffffff;
    --ink: #111111;
    --frame: #222222;
    --label: #333333;
    --green: #0e8844;
    --band-text: #7cc196;
    --silver: #959595;
  }
  html, body {
    margin: 0;
    padding: 0;
    width: 1200px;
    height: 927px;
    overflow: hidden;
    background: var(--page);
    font-family: "Oswald", "Arial Narrow", sans-serif;
  }
  .sheet {
    position: relative;
    width: 1200px;
    height: 927px;
  }
  .side {
    position: absolute;
    top: 102px;
    width: 380px;
  }
  .side--front { left: 176px; }
  .side--back { left: 629px; }
  .side-label {
    margin: 0 0 45px;
    text-align: center;
    font-weight: 300;
    font-size: 14px;
    color: var(--label);
  }
  .card {
    position: relative;
    box-sizing: border-box;
    width: 380px;
    height: 218px;
    border: 1px solid var(--frame);
    background: var(--page);
    overflow: hidden;
  }
  .brand {
    position: absolute;
    left: 0;
    right: 0;
    margin: 0;
    text-align: center;
    font-weight: 600;
    text-transform: uppercase;
    letter-spacing: 1px;
    line-height: 1;
  }
  .card--front .brand {
    top: 34px;
    font-size: 30px;
    color: var(--ink);
  }
  .card--back .brand {
    top: 78px;
    font-size: 46px;
    color: var(--silver);
  }
  .person {
    position: absolute;
    top: 109px;
    left: 0;
    right: 0;
    text-align: center;
  }
  .person-name {
    margin: 0;
    font-weight: 500;
    font-size: 19px;
    line-height: 1.1;
    color: var(--ink);
  }
  .person-role {
    margin: 2px 0 0;
    font-weight: 300;
    font-size: 14px;
    letter-spacing: 0.6px;
    color: var(--ink);
  }
  .contact-band {
    position: absolute;
    left: 0;
    right: 0;
    bottom: 0;
    height: 31px;
    padding: 0 6px;
    display: flex;
    justify-content: space-between;
    align-items: center;
    background: var(--green);
    color: var(--band-text);
    font-weight: 300;
    font-size: 14px;
  }
</style>
</head>
<body>
  <main class="sheet">
    <section class="side side--front">
      <p class="side-label">Front</p>
      <article class="card card--front">
        <p class="brand">Tovrak Regional</p>
        <div class="person">
          <p class="person-name">Daniel Hartwell</p>
          <p class="person-role">Chief Executive Officer</p>
        </div>
        <footer class="contact-band">
          <span class="contact-phone">P: 0400 555 219</span>
          <span class="contact-email">daniel@tovrak.com.au</span>
        </footer>
      </article>
    </section>

    <section class="side side--back">
      <p class="side-label">Back</p>
      <article class="card card--back">
        <p class="brand">Tovrak Regional</p>
      </article>
    </section>
  </main>
</body>
</html>
```